Business Card for beauty technology startup

Design Glowra Business Card for a Beauty, based on the website identity and colors (https://www.glowra-example.com).
Glowra is a beauty tech startup that gathers helpful product info for beauty lovers and consumers (such as availability on stores, price range and product reviews) for makeup products. The card design must be young, colorful but clean, and very modern.

Target Market(s)

woman, 15-35

Industry/Entity Type

Cosmetics

Contact Information for Business Card

Full Name, address, phone

Font styles to use
Other font styles liked:
• Advent Pro

Colors
e34297
86cfc6
ffffff
5c5c5c
e8e8e8
e667a6
b2b2b2

Requirements
Must have
• One full colored side with a creative design and another with card info
• Use Color palette: #95C5C5 and/or #D38AA5
• Use fonts: Advent Pro
• Use website identity: https://www.glowra-example.com
Nice to have
• If needed extra font: Roboto

```html
<!DOCTYPE html>
<html lang="en">
<head>
<meta charset="utf-8">
<title>Glowra Business Card</title>
<link rel="stylesheet" href="https://fonts.googleapis.com/css2?family=Advent+Pro:wght@200;300;400;600;700&display=swap">
<style>
  :root {
    --teal: #86cfc6;
    --teal-deep: #6fb4ab;
    --teal-soft: #d6f0ec;
    --white: #ffffff;
    --ink: #2a2426;
    --grey: #5c5c5c;
    --backdrop: #e8e8e8;
  }
  * { margin: 0; padding: 0; box-sizing: border-box; }
  html, body { width: 1200px; height: 1200px; overflow: hidden; }
  body {
    background: var(--backdrop);
    font-family: "Advent Pro", sans-serif;
    position: relative;
  }
  .card {
    position: absolute;
    left: 180px;
    width: 840px;
    height: 480px;
    border-radius: 4px;
    overflow: hidden;
    box-shadow: 0 8px 24px rgba(0,0,0,0.15);
  }
  .card--front { top: 80px; background: var(--teal); }
  .card--back {
    top: 640px;
    background: linear-gradient(20deg, var(--teal) 0%, var(--teal-soft) 30%, var(--white) 55%);
  }
  .card__ring { position: absolute; }
  .card--front .card__ring { left: 40px; top: 60px; width: 380px; height: 380px; }
  .card--back .card__ring { left: 50px; top: 70px; width: 430px; height: 430px; }

  .front__brand {
    position: absolute;
    right: 36px;
    top: 30px;
    writing-mode: vertical-rl;
    font-weight: 200;
    font-size: 92px;
    letter-spacing: 18px;
    color: var(--teal-deep);
  }

  .back__brand {
    position: absolute;
    right: 60px;
    top: 44px;
    display: flex;
    align-items: center;
    gap: 22px;
  }
  .back__brand-dot {
    width: 70px; height: 70px;
    border: 3px solid var(--ink);
    border-radius: 50%;
  }
  .back__brand-name {
    font-weight: 300;
    font-size: 62px;
    letter-spacing: 12px;
    color: var(--ink);
  }
  .back__person {
    position: absolute;
    right: 60px;
    top: 150px;
    text-align: right;
  }
  .back__name {
    font-weight: 700;
    font-size: 40px;
    letter-spacing: 1px;
    color: var(--teal);
  }
  .back__role {
    font-weight: 400;
    font-size: 24px;
    color: var(--grey);
    margin-top: -4px;
  }
  .back__contacts {
    position: absolute;
    right: 56px;
    top: 262px;
    list-style: none;
    text-align: right;
  }
  .back__contacts li {
    display: flex;
    justify-content: flex-end;
    align-items: center;
    gap: 12px;
    font-size: 26px;
    font-weight: 400;
    color: var(--ink);
    margin-bottom: 8px;
  }
  .back__contacts svg { width: 24px; height: 24px; fill: var(--teal); }
  .back__rule {
    position: absolute;
    right: 56px;
    top: 382px;
    width: 440px;
    height: 2px;
    background: var(--teal);
  }
  .back__address {
    position: absolute;
    right: 56px;
    top: 396px;
    display: flex;
    align-items: center;
    gap: 12px;
    font-size: 26px;
    color: var(--ink);
  }
  .back__address svg { width: 24px; height: 24px; fill: var(--teal); }
</style>
</head>
<body>
  <section class="card card--front">
    <svg class="card__ring" viewBox="0 0 100 100" aria-hidden="true">
      <circle cx="50" cy="50" r="47" fill="none" stroke="#7cc2b9" stroke-width="1.2"/>
    </svg>
    <div class="front__brand">GLOWRA</div>
  </section>

  <section class="card card--back">
    <svg class="card__ring" viewBox="0 0 100 100" aria-hidden="true">
      <circle cx="50" cy="50" r="47" fill="none" stroke="#ffffff" stroke-width="1.4"/>
    </svg>
    <div class="back__brand">
      <span class="back__brand-dot"></span>
      <span class="back__brand-name">GLOWRA</span>
    </div>
    <div class="back__person">
      <div class="back__name">JOHN DOE</div>
      <div class="back__role">Director</div>
    </div>
    <ul class="back__contacts">
      <li>1-234-567890
        <svg viewBox="0 0 24 24" aria-hidden="true"><path d="M6.6 10.8a15 15 0 0 0 6.6 6.6l2.2-2.2a1 1 0 0 1 1-.25 11.4 11.4 0 0 0 3.6.57 1 1 0 0 1 1 1V20a1 1 0 0 1-1 1A17 17 0 0 1 3 4a1 1 0 0 1 1-1h3.5a1 1 0 0 1 1 1c0 1.25.2 2.45.57 3.6a1 1 0 0 1-.25 1z"/></svg>
      </li>
      <li>www.glowra-example.com
        <svg viewBox="0 0 24 24" aria-hidden="true"><path d="M12 2a10 10 0 1 0 0 20 10 10 0 0 0 0-20zm6.9 6h-2.9a15.6 15.6 0 0 0-1.4-3.6A8 8 0 0 1 18.9 8zM12 4a14 14 0 0 1 1.9 4h-3.8A14 14 0 0 1 12 4zM4.3 14a8 8 0 0 1 0-4h3.4a16 16 0 0 0 0 4zm.8 2h2.9a15.6 15.6 0 0 0 1.4 3.6A8 8 0 0 1 5.1 16zM8 8H5.1a8 8 0 0 1 4.3-3.6A15.6 15.6 0 0 0 8 8zm4 12a14 14 0 0 1-1.9-4h3.8A14 14 0 0 1 12 20zm2.3-6H9.7a14.7 14.7 0 0 1 0-4h4.6a14.7 14.7 0 0 1 0 4zm.3 5.6a15.6 15.6 0 0 0 1.4-3.6h2.9a8 8 0 0 1-4.3 3.6zm1.7-5.6a16 16 0 0 0 0-4h3.4a8 8 0 0 1 0 4z"/></svg>
      </li>
    </ul>
    <div class="back__rule"></div>
    <div class="back__address">Dummy city, Dummy Country Land
      <svg viewBox="0 0 24 24" aria-hidden="true"><path d="M12 2a7 7 0 0 0-7 7c0 5.2 7 13 7 13s7-7.8 7-13a7 7 0 0 0-7-7zm0 9.5A2.5 2.5 0 1 1 12 6.5a2.5 2.5 0 0 1 0 5z"/></svg>
    </div>
  </section>
</body>
</html>
```